Business card - house cleaning company

We want friendly high end business card highlighting our services . NO LOGOs on back of card please.. no vertical cards NO DOUBLE BROOMS

2 owners of the company: Corinne Hale & Dean Oakley

Included phone number: (555)318-2207

Email: brightnookclean@example.net

Website: www.brightnookclean.example

Bonded & Insured

Fernhaven, FH 80999

Slogan maybe: Bringing a brighter shine to every room you love

We want elegant high end card for house cleaning service. Maybe 2 sided if needed. Can it have bullet points of some services we offer

Residential Home Cleaning
Vacation Rental Cleaning
Commercial Cleaning
Carpet Cleaning
Window Cleaning
Property Management
Property Inspections
Property Maintenance
Trash Removal
Concierge Services

Highlight service on back of card. If we can do a one sided card with all this that’s great as well. Not cartoony.

Our logo attached and a design somone I had Harlan but they put very little time in. Not Unique enough. If you can do a custom design with a feminine touch that be great.

You will be eliminated for not reading the brief. NO DOUBLE LOGOS NO DOUBLE BROOMS. PLEASE BE CREATIVE. IF POST SAME LOGO WITH SMAL CHANGES RHEY WILL BE ELIMINATED. BE CREATIVE.
Updates

Thank you everyone for your designs. please only use the logo 1 time. and would love to see some that dont look all the same. We appreciate your time.

Target Market(s)

Residential and vacation rental home cleaning maid service

Industry/Entity Type

House cleaning maid services

Contact Information for Business Card

For business card use logo. black and green one provided. others for example. I wil try find some example.. We want friendly high end look. 2 owners of the company: Corinne Hale & Dean Oakley Included phone number: (555)318-2207 Email: brightnookclean@example.net Website: www.brightnookclean.example Bonded & Insured Fernhaven, FH Slogan maybe: Bringing a brighter shine to every room you love or Quality Service Guaranteed We want elegant high end card for house cleaning service. Maybe 2 sided if needed. Can it have bullet points of some services we offer Residential Home Cleaning Vacation Rental Cleaning Commercial Cleaning Carpet Cleaning Window Cleaning Property Management Property Inspections Property Maintenance Trash Removal Concierge Services

Requirements
Must have
• For business card use logo . Creativity. black and green one provided. We want friendly high end look. 2 owners of the company: Corinne Hale & Dean Oakley Included phone number: (555)318-2207 Email: brightnookclean@example.net Website: www.brightnookclean.example Licensed Bonded & Insured Fernhaven, FH Slogan maybe: Bringing a brighter shine to every room you love or Quality Service Guaranteed We want elegant high end card for house cleaning service. Maybe 2 sided if needed. Can it have bullet points of some services we offer Residential Home Cleaning Vacation Rental Cleaning Commercial Cleaning Carpet Cleaning Window Cleaning Property Management Property Inspections Property Maintenance Trash Removal Concierge Services .. creatitivty a plus. whimsical. we like stars..
Nice to have
• we want much better than the example of biz card provided as example. logo has colors that are in our website palette as well. We are open to ideas for the business card design. Will pay tip to best work. PLEASE USE COMPLIMENTING COLORS. . WE LIKE BLACK AND WHITE, stars
Should not have
• NO DOUBLE LOGOS. READ READ. READ. YOU WILL BE ELIMINATED no double logos or double brooms same side of card. I want didfrent examples. please don't make all your submission look the same

```html
<!DOCTYPE html>
<html lang="en">
<head>
<meta charset="utf-8">
<title>Bright Nook Cleaning Services – Business Card</title>
<link rel="stylesheet" href="https://fonts.googleapis.com/css2?family=Source+Sans+3:wght@400;600;700&display=swap">
<style>
  :root {
    --backdrop: #737373;
    --card-white: #ffffff;
    --brand-blue: #2d6890;
    --brand-green: #6e9a46;
    --ink: #111111;
  }
  * { box-sizing: border-box; margin: 0; padding: 0; }
  html, body { width: 1200px; height: 1200px; overflow: hidden; }
  body {
    background: var(--backdrop);
    font-family: "Source Sans 3", Arial, sans-serif;
    position: relative;
  }
  .card {
    position: absolute;
    width: 644px;
    height: 368px;
    box-shadow: 6px 8px 14px rgba(0,0,0,0.25);
  }
  .card-front { left: 116px; top: 163px; background: var(--card-white); }
  .card-back { left: 438px; top: 642px; background: var(--brand-blue); }

  .brand-name {
    position: absolute;
    left: 35px; top: 112px;
    width: 260px;
    text-align: center;
    color: var(--brand-blue);
    font-weight: 600;
    line-height: 1;
  }
  .brand-name .brand-main { display: block; font-size: 44px; letter-spacing: -0.5px; }
  .brand-name .brand-sub { display: block; font-size: 15px; letter-spacing: 1.2px; margin-top: 6px; }

  .front-divider {
    position: absolute;
    left: 322px; top: 66px;
    width: 2px; height: 180px;
    background: var(--brand-blue);
  }
  .owner-name {
    position: absolute;
    left: 345px; top: 61px;
    font-size: 32px;
    font-weight: 700;
    color: var(--ink);
    letter-spacing: 0.3px;
    border-bottom: 1.5px solid var(--ink);
    line-height: 1.05;
  }
  .contact-list {
    position: absolute;
    left: 346px; top: 114px;
    list-style: none;
  }
  .contact-list li {
    display: flex;
    align-items: center;
    height: 24px;
    font-size: 18px;
    color: var(--ink);
  }
  .contact-icon {
    width: 19px; height: 19px;
    margin-right: 8px;
    flex: none;
  }
  .credential {
    position: absolute;
    left: 345px; top: 223px;
    font-size: 17.5px;
    color: var(--ink);
  }
  .accent-rule {
    position: absolute;
    left: 0; top: 315px;
    width: 100%; height: 4px;
    background: var(--brand-green);
  }
  .slogan-band {
    position: absolute;
    left: 0; top: 323px;
    width: 100%; height: 45px;
    background: var(--brand-blue);
    color: #fff;
    font-size: 22.5px;
    text-align: center;
    line-height: 45px;
    letter-spacing: 0.2px;
    white-space: nowrap;
  }

  .service-list {
    position: absolute;
    top: 124px;
    list-style: none;
  }
  .service-list.left { left: 66px; }
  .service-list.right { left: 343px; }
  .service-list li {
    display: flex;
    align-items: center;
    height: 24.2px;
    font-size: 19.5px;
    color: #fff;
  }
  .tick { width: 15px; height: 15px; margin-right: 5px; flex: none; }
  .back-divider {
    position: absolute;
    left: 322px; top: 114px;
    width: 2px; height: 139px;
    background: var(--brand-green);
  }
</style>
</head>
<body>
  <section class="card card-front">
    <div class="brand-name"><span class="brand-main">Bright Nook</span><span class="brand-sub">CLEANING SERVICES</span></div>
    <div class="front-divider"></div>
    <h1 class="owner-name">CORINNE HALE</h1>
    <ul class="contact-list">
      <li>
        <svg class="contact-icon" viewBox="0 0 20 20"><rect width="20" height="20" rx="2" fill="#6e9a46"/><path d="M6.2 4.5l2 2.3-1 1.3c.8 1.7 2 2.9 3.7 3.7l1.3-1 2.3 2-1.2 1.7C9.5 14.3 5.7 10.5 4.5 6z" fill="#fff"/></svg>
        <span>&nbsp;(555)318-2207</span>
      </li>
      <li>
        <svg class="contact-icon" viewBox="0 0 20 20"><rect width="20" height="20" rx="2" fill="#6e9a46"/><text x="10" y="14.5" font-size="13" text-anchor="middle" fill="#fff" font-family="Arial, sans-serif">@</text></svg>
        <span>brightnookclean@example.net</span>
      </li>
      <li>
        <svg class="contact-icon" viewBox="0 0 20 20"><rect width="20" height="20" rx="2" fill="#6e9a46"/><g fill="none" stroke="#fff" stroke-width="1"><circle cx="10" cy="10" r="5.5"/><ellipse cx="10" cy="10" rx="2.4" ry="5.5"/><path d="M4.5 10h11M5.3 7.2h9.4M5.3 12.8h9.4"/></g></svg>
        <span>www.brightnookclean.example</span>
      </li>
      <li>
        <svg class="contact-icon" viewBox="0 0 20 20"><rect width="20" height="20" rx="2" fill="#6e9a46"/><path d="M10 3.5a4.5 4.5 0 0 0-4.5 4.5c0 3.3 4.5 8.5 4.5 8.5s4.5-5.2 4.5-8.5A4.5 4.5 0 0 0 10 3.5z" fill="#fff"/><circle cx="10" cy="8" r="1.7" fill="#6e9a46"/></svg>
        <span>Fernhaven, FH 80999</span>
      </li>
    </ul>
    <p class="credential">BONDED &amp; INSURED</p>
    <div class="accent-rule"></div>
    <p class="slogan-band">BRINGING A BRIGHTER SHINE TO EVERY ROOM YOU LOVE</p>
  </section>

  <section class="card card-back">
    <ul class="service-list left">
      <li><svg class="tick" viewBox="0 0 14 14"><circle cx="7" cy="7" r="6.5" fill="#fff"/><path d="M3.5 7l2.5 2.8L12.5 2" fill="none" stroke="#6e9a46" stroke-width="2.2"/></svg>Residential Home Cleaning</li>
      <li><svg class="tick" viewBox="0 0 14 14"><circle cx="7" cy="7" r="6.5" fill="#fff"/><path d="M3.5 7l2.5 2.8L12.5 2" fill="none" stroke="#6e9a46" stroke-width="2.2"/></svg>Vacation Rental Cleaning</li>
      <li><svg class="tick" viewBox="0 0 14 14"><circle cx="7" cy="7" r="6.5" fill="#fff"/><path d="M3.5 7l2.5 2.8L12.5 2" fill="none" stroke="#6e9a46" stroke-width="2.2"/></svg>Commercial Cleaning</li>
      <li><svg class="tick" viewBox="0 0 14 14"><circle cx="7" cy="7" r="6.5" fill="#fff"/><path d="M3.5 7l2.5 2.8L12.5 2" fill="none" stroke="#6e9a46" stroke-width="2.2"/></svg>Carpet Cleaning</li>
      <li><svg class="tick" viewBox="0 0 14 14"><circle cx="7" cy="7" r="6.5" fill="#fff"/><path d="M3.5 7l2.5 2.8L12.5 2" fill="none" stroke="#6e9a46" stroke-width="2.2"/></svg>Window Cleaning</li>
    </ul>
    <div class="back-divider"></div>
    <ul class="service-list right">
      <li><svg class="tick" viewBox="0 0 14 14"><circle cx="7" cy="7" r="6.5" fill="#fff"/><path d="M3.5 7l2.5 2.8L12.5 2" fill="none" stroke="#6e9a46" stroke-width="2.2"/></svg>Property Management</li>
      <li><svg class="tick" viewBox="0 0 14 14"><circle cx="7" cy="7" r="6.5" fill="#fff"/><path d="M3.5 7l2.5 2.8L12.5 2" fill="none" stroke="#6e9a46" stroke-width="2.2"/></svg>Property Inspections</li>
      <li><svg class="tick" viewBox="0 0 14 14"><circle cx="7" cy="7" r="6.5" fill="#fff"/><path d="M3.5 7l2.5 2.8L12.5 2" fill="none" stroke="#6e9a46" stroke-width="2.2"/></svg>Property Maintenance</li>
      <li><svg class="tick" viewBox="0 0 14 14"><circle cx="7" cy="7" r="6.5" fill="#fff"/><path d="M3.5 7l2.5 2.8L12.5 2" fill="none" stroke="#6e9a46" stroke-width="2.2"/></svg>Trash Removal</li>
      <li><svg class="tick" viewBox="0 0 14 14"><circle cx="7" cy="7" r="6.5" fill="#fff"/><path d="M3.5 7l2.5 2.8L12.5 2" fill="none" stroke="#6e9a46" stroke-width="2.2"/></svg>Concierge Services</li>
    </ul>
  </section>
</body>
</html>
```